Training Company Needs a Web Design

We are a Training company that needs a website design completed for us. "The Harbor Loft" The website will be a 'community space' specialising in 'Change and Transformation'. It will be a 'space' where individuals can come to find out 'latest news', upcoming events and courses, chat with others and find 'tools and templates'. They will need to login as a 'Member'.

The final design needs to be professional but have a 'fun and interactive' feel and appeal to our target audience who are predominantly corporate individuals.

Target Market(s)

Corporate Individuals - they may have a Change or Project background

Industry/Entity Type

Business Consultant

Number of Pages Required

3 page

Font styles to use
Sans Serif

Requirements
Must have
• Design for 'Home Page'
• A professional and corporate 'feel' but be fun and interactive.
Nice to have
• A 'sense' of how some of the other pages may be designed or laid out.

```html
<!DOCTYPE html>
<html lang="en">
<head>
<meta charset="utf-8">
<title>The Harbor Loft – Home</title>
<link rel="stylesheet" href="https://fonts.googleapis.com/css2?family=Lato:wght@300;400;700;900&family=Oswald:wght@400;500&display=swap">
<style>
:root{
  --ink:#2b2b2b;
  --text:#444;
  --muted:#777;
  --dark:#333333;
  --darker:#2a2a2a;
  --accent:#1a9fd6;
  --navy:#0d4f8b;
  --teal:#3fcbb0;
  --light:#eeeeee;
  --line:#d6d6d6;
  --white:#ffffff;
}
*{box-sizing:border-box;margin:0;padding:0}
html,body{width:1200px;height:3502px;overflow:hidden}
body{font-family:"Lato",Arial,sans-serif;color:var(--text);background:var(--white);position:relative}
.sec{position:absolute;left:0;width:1200px}
.title{position:absolute;left:0;width:100%;text-align:center;font-weight:400;font-size:40px;letter-spacing:1px;color:var(--ink)}
.title span{color:var(--accent)}
.divider{position:absolute;left:580px;width:40px;height:2px;background:var(--accent)}
.btn{position:absolute;background:var(--teal);color:var(--dark);font-size:15px;font-weight:700;text-transform:uppercase;display:flex;align-items:center;justify-content:center;border-radius:3px}

/* top bar */
.topbar{top:0;height:24px;background:var(--darker)}
.topbar .auth{position:absolute;right:20px;top:0;height:24px;display:flex;gap:28px;align-items:center;color:#ccc;font-size:13px}
.topbar .auth i{display:inline-block;width:10px;height:10px;border-radius:50%;background:var(--teal);margin-right:6px;vertical-align:-1px}

/* header */
.header{top:24px;height:112px;background:var(--white)}
.brand{position:absolute;left:133px;top:30px;display:flex;align-items:center;gap:14px;font-weight:700;font-size:26px;line-height:1;color:var(--navy);letter-spacing:1px}
.brand i{width:22px;height:22px;background:var(--accent);border-radius:50%}
.contact-chip{position:absolute;top:38px;display:flex;gap:14px;align-items:center;font-size:16px;color:var(--ink);line-height:1.3}
.contact-chip svg{width:34px;height:34px}
.live-chat{position:absolute;left:848px;top:54px;width:128px;height:52px;background:var(--teal);border-radius:4px;color:var(--dark);font-weight:900;font-size:17px;line-height:1;padding:8px 10px}
.live-chat small{display:block;font-size:14px;font-weight:700;margin-bottom:4px}
.agent{position:absolute;left:976px;top:20px;width:92px;height:92px;background:linear-gradient(#c9d3da,#8a9aa6)}

/* nav */
.mainnav{top:136px;height:44px;background:var(--dark)}
.mainnav ul{list-style:none;display:flex;position:absolute;left:133px;top:0;height:44px}
.mainnav li{width:150px;display:flex;align-items:center;justify-content:center;color:#e6e6e6;font-size:16px;letter-spacing:1px;border-right:1px solid #555}
.mainnav li:last-child{border-right:0}
.mainnav li.active{background:#2d6fab;color:var(--white)}

/* hero */
.hero{top:180px;height:535px;background:linear-gradient(180deg,#9fb1c2 0%,#64788c 45%,#3b3f44 75%,#1f2226 100%)}
.hero h1{position:absolute;left:0;width:100%;top:295px;text-align:center;font-family:"Oswald",Arial,sans-serif;font-weight:400;font-size:40px;color:var(--white);letter-spacing:1px}
.dots{position:absolute;top:498px;left:548px;display:flex;gap:12px}
.dots i{width:14px;height:14px;border-radius:50%;background:#ddd;display:block}
.dots i:first-child{background:none;border:2px solid #ddd}

/* welcome */
.welcome{top:715px;height:389px;background:linear-gradient(160deg,#f4f4f4,#e4e4e4)}
.welcome p.lead{position:absolute;left:148px;width:904px;top:137px;text-align:center;font-size:15px;line-height:23px;color:#555}
.pillar{position:absolute;top:260px;display:flex;gap:18px;align-items:center}
.pillar svg{width:100px;height:100px}
.pillar h3{font-size:20px;font-weight:400;color:var(--ink);margin-bottom:10px}
.pillar p{font-size:13px;line-height:18px;color:#666;width:200px}

/* services */
.services{top:1104px;height:523px;background:var(--navy)}
.services .title{color:var(--white)}
.service{position:absolute;top:122px;width:437px}
.service .photo{height:168px;border:1px solid #9bb6d1}
.service h3{margin-top:32px;font-size:28px;font-weight:400;letter-spacing:1px;color:var(--white)}
.service p{margin-top:10px;font-size:14px;line-height:18px;color:#e4ecf4}
.service .btn{position:static;margin-top:16px;width:116px;height:32px;font-size:13px}

/* events */
.events{top:1627px;height:535px;background:var(--white)}
.arrow{position:absolute;top:215px;width:22px;height:40px}
.card{position:absolute;top:141px;width:222px}
.card .photo{height:175px;border:4px solid #ddd}
.card h4{margin-top:24px;font-size:16px;font-weight:700;color:var(--navy)}
.card .date{margin-top:8px;font-size:12px;color:#888}
.card p{margin-top:6px;font-size:13px;line-height:16px;color:#444}
.card .btn{position:static;margin-top:20px;width:116px;height:32px;font-size:13px}

/* tools */
.tools{top:2162px;height:386px;background:#efefef}
.tools p{position:absolute;left:130px;width:940px;top:140px;text-align:center;font-size:17px;line-height:28px;color:#444}
.select{position:absolute;left:455px;top:224px;width:290px;height:47px;background:var(--white);border:1px solid #ddd;display:flex;align-items:center;padding-left:22px;font-size:14px;color:#444}
.select b{position:absolute;right:0;top:0;width:50px;height:45px;border-left:1px solid #ddd;display:flex;align-items:center;justify-content:center}
.tools .go{position:absolute;left:535px;top:299px;width:133px;height:44px;background:#111;color:var(--white);font-size:15px;font-weight:700;display:flex;align-items:center;justify-content:center;border-radius:2px}

/* why */
.why{top:2548px;height:413px}
.why .panel{position:absolute;left:0;top:0;width:607px;height:413px;background:var(--dark);padding:36px 0 0 133px}
.why h2{font-size:28px;font-weight:400;color:var(--white);letter-spacing:1px}
.why .intro{margin-top:14px;font-size:14px;line-height:20px;color:#e8e8e8;width:420px}
.why ul{list-style:none;margin-top:14px}
.why li{display:flex;gap:12px;font-size:13px;font-weight:700;color:var(--white);line-height:17px;margin-bottom:19px;width:420px}
.why li svg{flex:none;width:15px;height:15px;margin-top:1px}
.why .photo{position:absolute;left:607px;top:0;width:593px;height:413px;background:linear-gradient(135deg,#b8a58a,#8f7c63 50%,#a9b8bd)}

/* footer nav */
.footnav{top:2961px;height:70px;background:var(--white)}
.footnav ul{list-style:none;display:flex;justify-content:center;height:70px;align-items:center}
.footnav li{padding:0 48px;font-size:16px;color:var(--ink);border-right:1px solid #999;line-height:18px}
.footnav li:last-child{border-right:0}

/* contact */
.contact{top:3031px;height:413px;background:linear-gradient(160deg,#f2f2f2,#e2e2e2)}
.contact h3{position:absolute;left:133px;top:146px;font-size:20px;font-weight:400;color:var(--ink);letter-spacing:1px}
.field{position:absolute;background:var(--white);font-size:13px;color:#333;padding:12px 12px}
.send{position:absolute;left:423px;top:317px;width:268px;height:40px;background:var(--navy);color:var(--white);font-size:14px;display:flex;align-items:center;justify-content:center;letter-spacing:.5px}
.info{position:absolute;left:761px;display:flex;gap:30px}
.info svg{width:20px;height:20px;flex:none}
.info h5{font-size:18px;font-weight:400;color:var(--ink)}
.info p{font-size:15px;line-height:20px;color:#333;margin-top:2px}

/* bottom bar */
.bottom{top:3444px;height:58px;background:var(--darker)}
.bottom p{position:absolute;left:133px;top:20px;font-size:14px;color:#ddd}
.social{position:absolute;right:133px;top:14px;display:flex;gap:10px}
.social i{width:30px;height:30px;border-radius:50%;background:var(--white);display:block}
</style>
</head>
<body>

<div class="sec topbar">
  <div class="auth"><span><i></i>Log In</span><span><i></i>Sign Up</span></div>
</div>

<header class="sec header">
  <div class="brand"><i></i>THE HARBOR LOFT</div>
  <div class="contact-chip" style="left:425px">
    <svg viewBox="0 0 34 34"><path d="M10 5l5 6-3 4c2 4 5 7 9 9l4-3 6 5-4 5C15 30 4 19 5 9z" fill="none" stroke="#1a9fd6" stroke-width="2.2"/></svg>
    <div>Call Us:<br>555-014-2200</div>
  </div>
  <div class="contact-chip" style="left:595px">
    <svg viewBox="0 0 34 34"><path d="M4 9h26v17H4z M4 9l13 10 13-10" fill="none" stroke="#1a9fd6" stroke-width="2.2"/></svg>
    <div>Mail Us:<br>info@theharborloft.com</div>
  </div>
  <div class="live-chat"><small>LIVE CHAT</small>ONLINE</div>
  <div class="agent" role="img" aria-label="Support agent wearing a headset"></div>
</header>

<nav class="sec mainnav">
  <ul><li class="active">HOME</li><li>ABOUT US</li><li>SERVICES</li><li>SOLUTIONS</li><li>BLOG</li><li>CONTACT US</li></ul>
</nav>

<section class="sec hero" role="img" aria-label="Silhouetted business team in a meeting room against a bright window">
  <h1>WE SPECIALIZE IN CHANGE &amp; TRANSFORMATION</h1>
  <div class="dots"><i></i><i></i><i></i><i></i></div>
</section>

<section class="sec welcome">
  <h2 class="title" style="top:48px">WELCOME TO <span>THE HARBOR LOFT</span></h2>
  <div class="divider" style="top:102px"></div>
  <p class="lead">Sed ut perspiciatis unde omnis iste natus error sit voluptatem accusantium dolo remque laudantium, totam rem aperiam, eaque ipsa quae ab illo inventore veritatis et quasi architecto beatae vitae dicta sunt explicabo. Sed ut perspiciatis unde omnis iste natus error sit voluptatem accusantium dolo. Sed ut perspiciatis unde omnis iste natus error sit voluptatem accusantium dolo.Sed ut perspiciatis unde omnis iste natus error sit voluptatem accusantium dolo.</p>
  <div class="pillar" style="left:305px">
    <svg viewBox="0 0 100 100"><circle cx="50" cy="50" r="44" fill="none" stroke="#0d4f8b" stroke-width="7"/><circle cx="50" cy="42" r="8" fill="#1a9fd6"/><circle cx="34" cy="58" r="7" fill="#1a9fd6"/><circle cx="66" cy="58" r="7" fill="#1a9fd6"/></svg>
    <div><h3>WHO WE ARE</h3><p>Sed ut perspiciatis unde omnis iste natus .</p></div>
  </div>
  <div class="pillar" style="left:652px">
    <svg viewBox="0 0 100 100"><circle cx="50" cy="50" r="44" fill="none" stroke="#0d4f8b" stroke-width="7"/><circle cx="50" cy="54" r="18" fill="none" stroke="#1a9fd6" stroke-width="5"/><circle cx="50" cy="54" r="6" fill="#1a9fd6"/></svg>
    <div><h3>OUR VISION</h3><p>Sed ut perspiciatis unde omnis iste natus .</p></div>
  </div>
</section>

<section class="sec services">
  <h2 class="title" style="top:44px">OUR SERVICES</h2>
  <div class="divider" style="top:94px;background:#7fb4e0"></div>
  <article class="service" style="left:131px">
    <div class="photo" role="img" aria-label="Trainer presenting to seated colleagues at a whiteboard" style="background:linear-gradient(135deg,#f2f2f2,#c7cdd3)"></div>
    <h3>CHANGE</h3>
    <p>Lorem ipsum dolor sit amet, consectetur adipiscing elit. Pellentesque sed odio ac tortor lobortis auctor sit amet id lectus. Vivamus in sodales eros. Ut pharetra, sapien at condimentum mollis, mi magna eleifend sapien, non hendrerit risus</p>
    <div class="btn">Read More</div>
  </article>
  <article class="service" style="left:630px">
    <div class="photo" role="img" aria-label="Goldfish leaping between two glass bowls under a blue sky" style="background:linear-gradient(180deg,#4f8fd0,#a7c9e8 55%,#5a8fb8)"></div>
    <h3>TRANSFORMATION</h3>
    <p>Lorem ipsum dolor sit amet, consectetur adipiscing elit. Pellentesque sed odio ac tortor lobortis auctor sit amet id lectus. Vivamus in sodales eros. Ut pharetra, sapien at condimentum mollis, mi magna eleifend sapien, non hendrerit risus</p>
    <div class="btn">Read More</div>
  </article>
</section>

<section class="sec events">
  <h2 class="title" style="top:30px">UPCOMING EVENT <span>&amp; COURSE</span></h2>
  <div class="divider" style="top:86px"></div>
  <svg class="arrow" style="left:82px" viewBox="0 0 22 40"><path d="M18 4L4 20l14 16" fill="none" stroke="#bbb" stroke-width="3"/></svg>
  <svg class="arrow" style="left:1096px" viewBox="0 0 22 40"><path d="M4 4l14 16L4 36" fill="none" stroke="#bbb" stroke-width="3"/></svg>
  <article class="card" style="left:133px">
    <div class="photo" role="img" aria-label="Group workshop around a table" style="background:linear-gradient(135deg,#c98f6a,#7d9a8c)"></div>
    <h4>LOREM IPSUM DOLOR SIT</h4><div class="date">20 FEB-2016</div>
    <p>Lorem ipsum dolor sit Lorem is the ipsum dolor sit Lorem ipsum dolor sit Lorem ipsum dolor sit</p>
    <div class="btn">Get Started</div>
  </article>
  <article class="card" style="left:371px">
    <div class="photo" role="img" aria-label="Team meeting in a bright office" style="background:linear-gradient(135deg,#e4e6e8,#8c98a4)"></div>
    <h4>LOREM IPSUM DOLOR SIT</h4><div class="date">20 FEB-2016</div>
    <p>Lorem ipsum dolor sit Lorem is the ipsum dolor sit Lorem ipsum dolor sit Lorem ipsum dolor sit</p>
    <div class="btn">Get Started</div>
  </article>
  <article class="card" style="left:607px">
    <div class="photo" role="img" aria-label="Colleagues discussing documents at a desk" style="background:linear-gradient(135deg,#b08a66,#4f4a48)"></div>
    <h4>LOREM IPSUM DOLOR SIT</h4><div class="date">20 FEB-2016</div>
    <p>Lorem ipsum dolor sit Lorem is the ipsum dolor sit Lorem ipsum dolor sit Lorem ipsum dolor sit</p>
    <div class="btn">Get Started</div>
  </article>
  <article class="card" style="left:845px">
    <div class="photo" role="img" aria-label="Course participants working together" style="background:linear-gradient(135deg,#d8d3cc,#7a6f6a)"></div>
    <h4>LOREM IPSUM DOLOR SIT</h4><div class="date">20 FEB-2016</div>
    <p>Lorem ipsum dolor sit Lorem is the ipsum dolor sit Lorem ipsum dolor sit Lorem ipsum dolor sit</p>
    <div class="btn">Get Started</div>
  </article>
</section>

<section class="sec tools">
  <h2 class="title" style="top:38px">FIND TOOLS <span>&amp; TEMPLATES</span></h2>
  <div class="divider" style="top:94px"></div>
  <p>Duis autem vel eum iriure ehendreritin vulputate velit esse molestie consequat, vel illum dolore eu feugiat nulla facilisis at vero eros et a molestie consequat,n et iusto velit esse molestie consequat, vel illum dolore</p>
  <div class="select">Tools And Templates<b><svg width="16" height="10" viewBox="0 0 16 10"><path d="M0 0h16L8 10z" fill="#888"/></svg></b></div>
  <div class="go">GET STARTED</div>
</section>

<section class="sec why">
  <div class="panel">
    <h2>WHY CHOOSE US</h2>
    <p class="intro">Lorem ipsum dolor sit amet consectetur adipiscing elit Pellentesque sed odio ac tortor lobortis auctor.</p>
    <ul>
      <li><svg viewBox="0 0 15 15"><circle cx="7.5" cy="7.5" r="7.5" fill="#fff"/><path d="M4 7.5l2.5 2.5L11 5" fill="none" stroke="#333" stroke-width="2"/></svg>Lorem ipsum dolor sit amet consectetur adipiscing elit</li>
      <li><svg viewBox="0 0 15 15"><circle cx="7.5" cy="7.5" r="7.5" fill="#fff"/><path d="M4 7.5l2.5 2.5L11 5" fill="none" stroke="#333" stroke-width="2"/></svg>Lorem ipsum dolor sit amet consectetur adipiscing elit</li>
      <li><svg viewBox="0 0 15 15"><circle cx="7.5" cy="7.5" r="7.5" fill="#fff"/><path d="M4 7.5l2.5 2.5L11 5" fill="none" stroke="#333" stroke-width="2"/></svg>Lorem ipsum dolor sit amet consectetur adipiscing elit</li>
      <li><svg viewBox="0 0 15 15"><circle cx="7.5" cy="7.5" r="7.5" fill="#fff"/><path d="M4 7.5l2.5 2.5L11 5" fill="none" stroke="#333" stroke-width="2"/></svg>Lorem ipsum dolor sit amet consectetur adipiscing elit</li>
      <li><svg viewBox="0 0 15 15"><circle cx="7.5" cy="7.5" r="7.5" fill="#fff"/><path d="M4 7.5l2.5 2.5L11 5" fill="none" stroke="#333" stroke-width="2"/></svg>Lorem ipsum dolor sit amet, consectetur adipiscing elit. Pellentesque sed odio ac tortor lobortis auctor</li>
      <li><svg viewBox="0 0 15 15"><circle cx="7.5" cy="7.5" r="7.5" fill="#fff"/><path d="M4 7.5l2.5 2.5L11 5" fill="none" stroke="#333" stroke-width="2"/></svg>Lorem ipsum dolor sit amet consectetur adipiscing elit</li>
    </ul>
  </div>
  <div class="photo" role="img" aria-label="Overhead view of a team meeting around a glass table on a wooden floor"></div>
</section>

<nav class="sec footnav">
  <ul><li>HOME</li><li>ABOUT US</li><li>SERVICES</li><li>SOLUTIONS</li><li>BLOG</li><li>CONTACT US</li></ul>
</nav>

<section class="sec contact">
  <h2 class="title" style="top:36px">CONTACT <span>US</span></h2>
  <div class="divider" style="top:92px"></div>
  <h3>AND WE WILL HELP YOU SHAPE YOUR FUTURE</h3>
  <div class="field" style="left:131px;top:201px;width:268px;height:40px">Enter Your Name</div>
  <div class="field" style="left:131px;top:261px;width:268px;height:40px">Enter Your Email</div>
  <div class="field" style="left:131px;top:317px;width:268px;height:40px">Phone</div>
  <div class="field" style="left:423px;top:201px;width:268px;height:100px">Message</div>
  <div class="send">SEND US YOUR INFORMATION</div>
  <div class="info" style="top:142px">
    <svg viewBox="0 0 20 20"><path d="M10 1a6 6 0 0 1 6 6c0 5-6 12-6 12S4 12 4 7a6 6 0 0 1 6-6z" fill="#222"/><circle cx="10" cy="7" r="2.2" fill="#eee"/></svg>
    <div><h5>Address Information</h5><p>Lorem ipsum dolor sit amet,<br>consectetur adipiscing</p></div>
  </div>
  <div class="info" style="top:236px">
    <svg viewBox="0 0 20 20"><path d="M2 5h16v11H2z" fill="#222"/><path d="M2 5l8 6 8-6" fill="none" stroke="#eee" stroke-width="1.5"/></svg>
    <div><h5 style="font-size:16px">Email</h5><p>info@theharborloft.com</p></div>
  </div>
  <div class="info" style="top:304px">
    <svg viewBox="0 0 20 20"><path d="M5 2l3 4-2 2c1 3 3 5 6 6l2-2 4 3-2 3C8 18 2 12 2 4z" fill="#222"/></svg>
    <div><h5 style="font-size:16px">Call Us</h5><p style="font-weight:700">555-014-2200</p></div>
  </div>
</section>

<footer class="sec bottom">
  <p>Copyright @ 2016 The Harbor Loft. All Rights Reserved.</p>
  <div class="social"><i></i><i></i><i></i><i></i></div>
</footer>

</body>
</html>
```